PITCH PRESENTATION for Feature Film Project

A while ago I had some key art designed for me for a film project called Cinderpeak's Heir (I see it's still in the online portfolio for inkharborstudio, who did the original work). I'm now taking that project to a series of pitch meetings at a film festival here in Canada and am putting together a powerpoint presentation.
I would want you to use the original design/aesthetic framework across the 14 pages of the presentation. I have provided the text and some image ideas (there's also one video to insert) that you may or may not use, etc. Probably for a large chunk of the pages - perhaps 6 of the ten - you could just clean it up and create a common background theme on which to place the companion text. Obviously, while making it pretty is a priority, it's also a priority for it to be legible to the people whom I'm pitching the project when it is projected onto a large screen.
I've uploaded a draft of the powerpoint text - there could be some minor changes between now and next week. I'll be leaving for the festival on December 3 so, obviously need a final version before that date. I've attached a .jpg of the original artwork along with the powerpoint.

Let me know if you need more details.

I wasn't able to upload the .psd file of the original poster artwork with layers & fonts but here is a link to download it from my dropbox: https://www.boxferrycloud.net/s/k3p8q2rz7tw5xym/GH-Cinderpeak%27s%20Heir%20poster.psd?dl=0 best Derek

This is targeted at some Chinese studio executives to whom the project will be pitched. It is for a film that is a martial arts thriller.

Festival

• The main thing is to use the already-existing material (the poster - incl colour scheme and fonts) as the aesthetic foundation for the presentation. We are, in a sense, trying to strengthen the brand identity of the project with the execs.

```html
<!DOCTYPE html>
<html lang="en">
<head>
<meta charset="utf-8">
<title>Roger Leung — Casting Ideas</title>
<link rel="stylesheet" href="https://fonts.googleapis.com/css2?family=Crimson+Text:wght@400;600&display=swap">
<style>
  :root {
    --ink-black: #0b0805;
    --umber-deep: #22170d;
    --umber-mid: #4a3419;
    --ochre-light: #7a5a2a;
    --ochre-glow: #8d6a34;
    --ember-orange: #e8781e;
    --paper-white: #f4f0ea;
    --blood-red: #6a1812;
    --blood-dark: #3c0f0a;
  }
  * { margin: 0; padding: 0; box-sizing: border-box; }
  html, body {
    width: 1200px;
    height: 675px;
    overflow: hidden;
    background: var(--ink-black);
  }
  .slide {
    position: relative;
    width: 1200px;
    height: 675px;
    overflow: hidden;
    font-family: "Crimson Text", Georgia, serif;
    color: var(--paper-white);
  }
  .slide-backdrop {
    position: absolute;
    inset: 0;
    background:
      /* dark silhouette of the head, top centre */
      radial-gradient(ellipse 11% 19% at 49% 14%, rgba(14,9,5,0.85), transparent 80%),
      /* blood-stained shirt, lower centre */
      radial-gradient(ellipse 16% 26% at 44% 92%, rgba(140,30,22,0.75), transparent 75%),
      radial-gradient(ellipse 26% 38% at 50% 82%, rgba(106,24,18,0.6), transparent 75%),
      /* shoulders of the figure */
      radial-gradient(ellipse 30% 32% at 50% 56%, rgba(60,15,10,0.55), transparent 75%),
      /* warm sepia light, upper right and centre */
      radial-gradient(ellipse 30% 40% at 72% 22%, rgba(141,106,52,0.75), transparent 75%),
      radial-gradient(ellipse 28% 36% at 30% 26%, rgba(122,90,42,0.55), transparent 75%),
      /* faded shop signage, lower right */
      radial-gradient(ellipse 12% 22% at 90% 86%, rgba(150,118,70,0.55), transparent 80%),
      /* aged wall, lower left */
      radial-gradient(ellipse 14% 24% at 8% 88%, rgba(96,72,40,0.45), transparent 80%),
      linear-gradient(90deg, var(--ink-black) 0%, var(--umber-deep) 14%, var(--umber-mid) 50%, var(--umber-deep) 88%, var(--ink-black) 100%);
  }
  .slide-grain {
    position: absolute;
    inset: 0;
    width: 1200px;
    height: 675px;
    opacity: 0.35;
    mix-blend-mode: overlay;
  }
  .slide-vignette {
    position: absolute;
    inset: 0;
    background: radial-gradient(ellipse 75% 80% at 50% 50%, transparent 55%, rgba(8,5,3,0.75) 100%);
  }
  .character-header {
    position: absolute;
    left: 72px;
    top: 36px;
  }
  .character-name {
    font-weight: 400;
    font-size: 58px;
    line-height: 1;
    color: var(--ember-orange);
  }
  .character-traits {
    margin-top: 6px;
    font-size: 34px;
    line-height: 1;
    color: var(--paper-white);
  }
  .casting-option {
    position: absolute;
    top: 205px;
  }
  .casting-photo {
    height: 280px;
  }
  .casting-name {
    margin-top: 18px;
    margin-left: 11px;
    font-size: 33px;
    line-height: 1;
  }
  .option-one { left: 67px; }
  .option-one .casting-photo {
    width: 313px;
    background: linear-gradient(135deg, #3b342c 0%, #1c1814 55%, #4a4036 100%);
  }
  .option-two { left: 462px; }
  .option-two .casting-photo {
    width: 296px;
    background: linear-gradient(160deg, #5d6b3e 0%, #a3262a 35%, #7d1b1e 65%, #2b2420 100%);
  }
  .option-three { left: 842px; }
  .option-three .casting-photo {
    width: 306px;
    background: linear-gradient(170deg, #5f8a8c 0%, #2e4a4d 45%, #b6931f 80%, #d3a92a 100%);
  }
</style>
</head>
<body>
  <main class="slide">
    <div class="slide-backdrop" role="img" aria-label="Key art backdrop: sepia grunge texture with a blurred figure seen from behind in a blood-stained shirt, swallow silhouettes and faded shop signs"></div>
    <svg class="slide-grain" viewBox="0 0 1200 675" aria-hidden="true">
      <filter id="paper-grain">
        <feTurbulence type="fractalNoise" baseFrequency="0.9" numOctaves="2" stitchTiles="stitch"/>
        <feColorMatrix type="saturate" values="0"/>
      </filter>
      <rect width="1200" height="675" filter="url(#paper-grain)"/>
    </svg>
    <div class="slide-vignette"></div>

    <header class="character-header">
      <h1 class="character-name">Roger Leung</h1>
      <p class="character-traits">Earnest, trustworthy, a rule-follower</p>
    </header>

    <figure class="casting-option option-one">
      <div class="casting-photo" role="img" aria-label="Actor photo: man in a dark jacket aiming a handgun"></div>
      <figcaption class="casting-name">Marcus Teo</figcaption>
    </figure>

    <figure class="casting-option option-two">
      <div class="casting-photo" role="img" aria-label="Actor photo: man in a black t-shirt aiming a pistol in front of a red truck"></div>
      <figcaption class="casting-name">Daniel Ohn</figcaption>
    </figure>

    <figure class="casting-option option-three">
      <div class="casting-photo" role="img" aria-label="Actor photo: man in a gold uniform shirt on a starship set"></div>
      <figcaption class="casting-name">Kevin Seo</figcaption>
    </figure>
  </main>
</body>
</html>
```